Buch-/eBook-Cover für populär-wissenschaftliches Buch
Zielgruppe
Der Talgrund-Verlag veröffentlicht Bücher zu psychologischen Themen. Dies ist ein eher populär wissenschaftliches Buch für eine breite Leserschaft.
Aufgabenstellung
Benötigt wird ein Buchcover für KTZ, Papierformat 158*223, Buchformat 154 x 3 x 217 mm 272 Normseiten
Kurzbeschreibung
Am Ufer getragen?
Fragen sich die Autoren Konrad Brüning und Matthias Oswerk. Zwei Psychoanalytiker mit langer Berufserfahrung. Geht das überhaupt: in Liebe und vereint zu sein? Dazu müssen zunächst andere Fragen geklärt werden.
Was vereint die Geschlechter, was bringt sie zusammen? Liebe? Dieses Wort gab es im Deutschen im frühen Mittelalter nicht, erst im späteren. In manchen Kulturen gibt es dieses Wort bis heute nicht, und dennoch leben Mann und Frau zusammen. Schon seit Jahrtausenden beschäftigt sich der Mensch mit der Beziehung zwischen den Geschlechtern. Philosophen, Schriftsteller, Dichter, Maler, Musiker, später Psychoanalytiker, Anthropologen und Soziologen hat die Beziehung zwischen Mann und Frau intensiv beschäftigt. Auch die Religionen befassen sich mit der Beziehung zwischen den Geschlechtern und zeigen vorwiegend auf moralischen und idealistischen Ebenen Umgangsweisen und Lebensformen zwischen den Geschlechtern auf.
280 Normseiten
Bitte Klappentext auf Rückseite

```html
<!DOCTYPE html>
<html lang="de">
<head>
<meta charset="utf-8">
<title>Am Ufer getragen? – Umschlag</title>
<link rel="stylesheet" href="https://fonts.googleapis.com/css2?family=Baloo+2:wght@400;600;700;800&family=Roboto+Condensed:wght@300;400&display=swap">
<style>
  :root {
    --paper: #ffffff;
    --ink: #141414;
    --terracotta: #c65f4f;
    --cover-light: #ffffff;
    --photo-dark: #2a1d19;
    --photo-mid: #7a4a34;
    --photo-warm: #c97a4a;
    --photo-glow: #e8a05c;
    --fold: #cfcfcf;
  }
  * { box-sizing: border-box; margin: 0; padding: 0; }
  html, body { width: 1200px; height: 632px; overflow: hidden; background: var(--paper); }
  body { position: relative; font-family: "Baloo 2", sans-serif; color: var(--ink); }

  .spread {
    position: absolute; left: 195px; top: 36px;
    width: 811px; height: 560px;
    display: flex;
    box-shadow: 0 2px 10px rgba(0,0,0,0.12);
  }

  .fold-mark {
    position: absolute; top: 18px; height: 596px; width: 1px;
    background: var(--fold);
  }
  .fold-mark--back { left: 573px; }
  .fold-mark--front { left: 628px; }

  /* Back cover */
  .back { position: relative; width: 378px; height: 100%; background: var(--paper); }
  .back__edge-photo {
    position: absolute; left: 0; top: 0; width: 24px; height: 100%;
    background: linear-gradient(180deg, var(--photo-glow) 0%, var(--photo-warm) 22%, var(--photo-mid) 55%, var(--photo-dark) 100%);
  }
  .back__band {
    position: absolute; left: 89px; top: 0; width: 224px; height: 46px;
    background: var(--terracotta);
    display: flex; align-items: center; justify-content: center;
  }
  .publisher-mark {
    font-family: "Baloo 2", sans-serif; font-weight: 600; font-size: 11px;
    color: var(--cover-light); display: flex; align-items: center; gap: 5px;
  }
  .publisher-mark__dot { width: 7px; height: 7px; border-radius: 50%; background: var(--cover-light); }

  .blurb {
    position: absolute; left: 53px; top: 70px; width: 296px;
    text-align: center; font-size: 9.4px; line-height: 13.8px;
  }
  .blurb__title { font-size: 19px; font-weight: 700; line-height: 22px; margin-bottom: 2px; }
  .blurb__lead { font-weight: 700; }
  .blurb p { margin-bottom: 7px; }

  .authors { position: absolute; left: 50px; top: 365px; width: 302px; text-align: center; font-size: 8.4px; line-height: 12.3px; }
  .authors__heading { margin-bottom: 7px; }
  .authors p { margin-bottom: 7px; }
  .authors strong { font-weight: 700; }

  /* Spine */
  .spine { position: relative; width: 55px; height: 100%; overflow: hidden; }
  .spine__photo {
    position: absolute; inset: 0;
    background: linear-gradient(180deg, var(--photo-mid) 0%, #5b3526 35%, #8a4e32 60%, var(--photo-dark) 100%);
  }
  .spine__text {
    position: absolute; left: 50%; top: 0; height: 100%;
    width: 55px;
  }
  .spine__title-block {
    position: absolute; left: 6px; bottom: 202px;
    transform: rotate(-90deg); transform-origin: left bottom;
    translate: 44px 0;
    white-space: nowrap; color: var(--cover-light);
  }
  .spine__title { font-family: "Baloo 2", sans-serif; font-weight: 800; font-size: 25px; line-height: 23px; letter-spacing: 0.5px; }
  .spine__subtitle { font-family: "Roboto Condensed", sans-serif; font-weight: 400; font-size: 10.6px; line-height: 11px; }
  .spine__authors {
    position: absolute; left: 30px; bottom: 28px;
    transform: rotate(-90deg); transform-origin: left bottom;
    translate: 8px 0;
    white-space: nowrap; color: var(--cover-light);
    font-family: "Roboto Condensed", sans-serif; font-weight: 400; font-size: 13px; line-height: 13px;
  }

  /* Front cover */
  .front { position: relative; width: 378px; height: 100%; overflow: hidden; }
  .front__photo {
    position: absolute; inset: 0;
    background:
      radial-gradient(ellipse at 75% 10%, rgba(232,160,92,0.55), transparent 55%),
      linear-gradient(180deg, #9a6a4c 0%, var(--photo-mid) 30%, #5e3a2c 60%, var(--photo-dark) 100%);
  }
  .front__band { position: absolute; left: 60px; top: 0; width: 224px; height: 46px; background: var(--terracotta); }
  .front__title {
    position: absolute; left: 0; width: 378px; top: 62px;
    text-align: center; color: var(--cover-light);
    font-family: "Baloo 2", sans-serif; font-weight: 800;
    font-size: 46px; line-height: 46px; letter-spacing: 1px;
  }
  .front__subtitle {
    position: absolute; left: 0; width: 378px; top: 158px; text-align: center;
    color: var(--cover-light); font-family: "Roboto Condensed", sans-serif; font-weight: 400; font-size: 14.5px;
  }
  .front__authors {
    position: absolute; left: 0; width: 378px; top: 508px; text-align: center;
    color: var(--cover-light); font-family: "Roboto Condensed", sans-serif; font-weight: 300; font-size: 21px;
  }
</style>
</head>
<body>
  <div class="fold-mark fold-mark--back"></div>
  <div class="fold-mark fold-mark--front"></div>

  <main class="spread">
    <section class="back">
      <div class="back__edge-photo" role="img" aria-label="Randstreifen des Umschlagfotos: Abendhimmel im Gegenlicht"></div>
      <div class="back__band">
        <span class="publisher-mark"><span class="publisher-mark__dot"></span>Talgrund-Verlag</span>
      </div>

      <div class="blurb">
        <h2 class="blurb__title">Am Ufer getragen?</h2>
        <p><span class="blurb__lead">Fragen sich die Autoren Konrad Brüning und Matthias Oswerk.</span><br>
        Zwei Psychoanalytiker mit langer Berufserfahrung.<br>
        Geht das überhaupt: in Liebe und vereint zu sein?<br>
        Dazu müssen zunächst andere Fragen geklärt werden.</p>
        <p>Was vereint die Geschlechter, was bringt sie zusammen? Liebe? Dieses Wort gab es im Deutschen im frühen Mittelalter nicht, erst im späteren. In manchen Kulturen gibt es dieses Wort bis heute nicht, und dennoch leben Mann und Frau zusammen. Schon seit Jahrtausenden beschäftigt sich der Mensch mit der Beziehung zwischen den Geschlechtern.</p>
        <p>Philosophen, Schriftsteller, Dichter, Maler, Musiker, später Psychoanalytiker, Anthropologen und Soziologen hat die Beziehung zwischen Mann und Frau intensiv beschäftigt. Auch die Religionen befassen sich mit der Beziehung zwischen den Geschlechtern und zeigen vorwiegend auf moralischen und idealistischen Ebenen Umgangsweisen und Lebensformen zwischen den Geschlechtern auf.</p>
      </div>

      <div class="authors">
        <h3 class="authors__heading" style="font-weight:400;font-size:8.4px;">DIE AUTOREN:</h3>
        <p><strong>KONRAD BRÜNING</strong> ist Diplom-Psychologe, Sozialwissenschaftler, Psychoanalytiker, Familientherapeut, Paartherapeut in eigener Praxis sowie Journalist und Filmemacher. Seit Jahren beforscht er die kulturellen Unterschiede in den Geschlechter und Familienbeziehungen verschiedener Kulturen (unter anderem in Ladakh, Himachal Pradesh, Namibia).</p>
        <p><strong>MATTHIAS OSWERK</strong> ist Facharzt für Psychotherapeutische Medizin und Psychoanalytiker. Er erforscht seit Jahren nach ethnoanalytischen Kriterien die Mosuo in China, eine der letzten matriarchalen Ethnien dieser Welt. Er erhielt den Prof. h.c. an der Nordhain-Universität Lindau.</p>
      </div>
    </section>

    <section class="spine">
      <div class="spine__photo" role="img" aria-label="Fortsetzung des Umschlagfotos: Paar vor warmer Abendlandschaft"></div>
      <div class="spine__title-block">
        <div class="spine__title">AM UFER GETRAGEN?</div>
        <div class="spine__subtitle">PSYCHOLOGISCHE FRAGEN UND HINTERGRÜNDE</div>
      </div>
      <div class="spine__authors">BRÜNING &amp; OSWERK</div>
    </section>

    <section class="front">
      <div class="front__photo" role="img" aria-label="Foto: Liebespaar Stirn an Stirn in einer Landschaft bei Sonnenuntergang mit Heißluftballons"></div>
      <div class="front__band"></div>
      <h1 class="front__title">AM UFER<br>GETRAGEN?</h1>
      <p class="front__subtitle">PSYCHOLOGISCHE FRAGEN UND HINTERGRÜNDE</p>
      <p class="front__authors">Brüning &amp; Oswerk</p>
    </section>
  </main>
</body>
</html>
```